Zielgruppe
TAKLEM verbindet künftige Auszubildende und Betriebe um Ausbildungsplätze optimal zu besetzen. Wir unterstützen Azubis bei der Suche nach einem geeigneten Ausbildungsplatz und vermitteln sie an einen für sie passenden Ausbildungsbetrieb.
Wir beraten individuell und nehmen uns für jeden einzelnen zu besetzenden Ausbildungsplatz und Azubi die Zeit, die er/sie verdient. Unsere Vernetzung im Münchner Raum und Umland ermöglicht es uns, Betriebe und Azubis erfolgreich zusammen zu bringen.
Aufgabenstellung
Bitte auch an Homepage/ Social Media Auftritt anlehnen.
Anzeige soll sowohl Jugendliche als auch Betriebe ansprechen.
Wir betreuen Azubis auf der Suche nach einem Ausbildungsplatz und suchen für Betriebe geeignete Auszibildende.
Für Betriebe suchen wir entweder per Direktauftrag oder es können Anzeigen auf der Homepage geschaltet werden.
Anzeige ist für ein 'Kolibo-Sammelheftt' des lokalen Fußballclubs geplant.
Die Anzeige wird aber noch für andere Medien verwendet, muss also allgemein gehalten sein.
Die Anzeige kann ggf auch zweigeteilt sein, einmal für Azubis, einmal für Betriebe die einen Azibi suchen
Anzeige ist 1/4 Seite A4 im Hochformat.
Anzeige brauche ich bitte im Hochformat in den Maßen: Höhe = 148 mm ; Breite = 105 mm (+ jeweils 3 mm Beschnittzugabe). Beschnittzugabe bedeutet, dass Sie in Ihrer Anzeige einen Rand von 3 mm einplanen müssen, sprich der bedruckte Bereich um 3 mm kleiner sein sollte als die Maße der Anzeige sind.
Die Anzeige sollte eine Auflösung von 300 dpi haben und sollte im PDF-Format sein.
Ich freue mich auf Eure Vorschläge

```html
<!DOCTYPE html>
<html lang="de">
<head>
<meta charset="utf-8">
<title>TAKLEM Anzeige</title>
<link href="https://fonts.googleapis.com/css2?family=Cabin:ital,wght@0,400;0,600;1,400&display=swap" rel="stylesheet">
<style>
  :root {
    --stage: #e9e9ec;
    --paper: #ffffff;
    --navy: #1f2d78;
    --blue: #2a4aa8;
    --blue-light: #4f64b2;
    --orange: #ee8a2c;
    --white: #ffffff;
    --ink-soft: #c9d0ee;
  }
  * { box-sizing: border-box; margin: 0; padding: 0; }
  html, body { width: 1200px; height: 800px; overflow: hidden; background: var(--stage); }
  body { font-family: "Cabin", "Gill Sans", sans-serif; position: relative; }

  .ad {
    position: absolute; left: 331px; top: 20px;
    width: 539px; height: 760px;
    background: var(--paper);
    overflow: hidden;
    box-shadow: 0 6px 24px rgba(0,0,0,.15);
  }
  .ad__shapes { position: absolute; inset: 0; }

  .brand {
    position: absolute; left: 34px; top: 40px;
    display: flex; flex-direction: column; align-items: center; gap: 8px;
  }
  .brand__mark { width: 22px; height: 22px; border-radius: 50%; background: var(--blue); }
  .brand__name { font-size: 21px; font-weight: 600; color: var(--blue); letter-spacing: .5px; }

  .headline {
    position: absolute; left: 52px; top: 350px; width: 440px;
    color: var(--white); font-size: 25px; font-style: italic; line-height: 1.3;
    transform: rotate(4deg); transform-origin: left top;
  }

  .services {
    position: absolute; left: 48px; top: 448px;
    list-style: none; color: var(--white); font-size: 18px;
  }
  .services li { display: flex; align-items: center; gap: 12px; margin-bottom: 14px; }
  .services__icon { width: 11px; height: 11px; flex: none; }

  .contacts { position: absolute; left: 0; top: 610px; list-style: none; }
  .contacts li { display: flex; align-items: center; height: 34px; margin-bottom: 10px; }
  .contacts__tab {
    width: 66px; height: 30px; background: var(--white);
    border-radius: 0 8px 8px 0; display: flex; align-items: center; justify-content: flex-end;
    padding-right: 10px; margin-right: 22px;
  }
  .contacts__tab svg { width: 16px; height: 16px; }
  .contacts__text { color: var(--white); font-size: 12px; }

  .cta {
    position: absolute; left: 338px; top: 628px; width: 180px;
    background: var(--orange); color: var(--white);
    font-size: 15px; font-style: italic; line-height: 1.3;
    padding: 10px 14px; border-radius: 4px;
  }
</style>
</head>
<body>
  <section class="ad" aria-label="Anzeige TAKLEM">
    <svg class="ad__shapes" viewBox="0 0 539 760" aria-hidden="false">
      <defs>
        <linearGradient id="panel" x1="0" y1="0" x2="1" y2="1">
          <stop offset="0" stop-color="#5b6cb6"/>
          <stop offset=".55" stop-color="#2c46a0"/>
          <stop offset="1" stop-color="#1a3590"/>
        </linearGradient>
        <linearGradient id="photo" x1="0" y1="0" x2="1" y2="0">
          <stop offset="0" stop-color="#c98a6a"/>
          <stop offset=".45" stop-color="#3a3f5c"/>
          <stop offset="1" stop-color="#d9dde6"/>
        </linearGradient>
      </defs>
      <rect x="80" y="30" width="450" height="300" fill="url(#photo)" opacity=".55"
            role="img" aria-label="Foto: ein junger Handwerker und eine junge Bürokauffrau vor einem Bildschirm mit der Website"/>
      <path d="M0 200 C150 285 330 325 430 285 C490 260 525 205 539 140 L539 760 L0 760 Z" fill="var(--orange)"/>
      <path d="M0 216 C150 302 330 342 432 302 C494 276 528 220 539 158 L539 760 L0 760 Z" fill="url(#panel)"/>
    </svg>

    <div class="brand">
      <span class="brand__mark"></span>
      <span class="brand__name">TAKLEM</span>
    </div>

    <p class="headline">Wir bringen die besten Azubis mit den besten Betrieben zusammen!</p>

    <ul class="services">
      <li><svg class="services__icon" viewBox="0 0 10 10"><path d="M5 0 L10 5 L5 10 L0 5 Z" fill="var(--orange)"/></svg>Individuelle Beratung</li>
      <li><svg class="services__icon" viewBox="0 0 10 10"><path d="M5 0 L10 5 L5 10 L0 5 Z" fill="var(--orange)"/></svg>Im Raum München &amp; Umland</li>
      <li><svg class="services__icon" viewBox="0 0 10 10"><path d="M5 0 L10 5 L5 10 L0 5 Z" fill="var(--orange)"/></svg>Vermittlung von Ausbildungssuchenden</li>
      <li><svg class="services__icon" viewBox="0 0 10 10"><path d="M5 0 L10 5 L5 10 L0 5 Z" fill="var(--orange)"/></svg>Vermittlung von Betrieben</li>
    </ul>

    <ul class="contacts">
      <li>
        <span class="contacts__tab"><svg viewBox="0 0 16 16"><path d="M4 1 L6.5 4.5 L5 6 C6 8.5 7.5 10 10 11 L11.5 9.5 L15 12 L13 15 C6.5 14 2 9.5 1 3 Z" fill="var(--orange)"/></svg></span>
        <span class="contacts__text">0152 40718255</span>
      </li>
      <li>
        <span class="contacts__tab"><svg viewBox="0 0 16 16"><rect x="1" y="3" width="14" height="10" rx="1" fill="var(--orange)"/><path d="M1.5 3.5 L8 9 L14.5 3.5" stroke="#fff" stroke-width="1.2" fill="none"/></svg></span>
        <span class="contacts__text">Jonas.Brehmer@taklem.de</span>
      </li>
      <li>
        <span class="contacts__tab"><svg viewBox="0 0 16 16"><circle cx="8" cy="8" r="7" fill="var(--orange)"/><path d="M1 8 H15 M8 1 C4 5 4 11 8 15 M8 1 C12 5 12 11 8 15" stroke="#fff" stroke-width="1" fill="none"/></svg></span>
        <span class="contacts__text">www.taklem.de</span>
      </li>
    </ul>

    <p class="cta">Interesse geweckt? Nehmen Sie gerne kostenlos Kontakt auf!</p>
  </section>
</body>
</html>
```